NORVANTEC IT SUPPORT WEBSITE AND CODING

We are a small IT Support company based if Broome Western Australia, we need to have our existing website www.norvantec.com.au converted or redesigned to a format that can be read on iphone , ipad and all browsers, must have facebook like button.

THIS PROJECT IS FOR DESIGN AND CODING OF COMPLETE WEBSITE.
Updates

Target Market(s)

Broome Local Businesses and Public.

Industry/Entity Type

It Company

Requirements
Must have
• Must be able to be viewed on all mobile devices , iphone , ipad , must have a facebook like button, the logo for norvanTEC is the way norvan tec is written in orange on the current website which is used on all our advertising which needs to stay the same or only change slightly.
Nice to have
• Contact us page that emails us.
Our address on a map.

```html
<!DOCTYPE html>
<html lang="en">
<head>
<meta charset="utf-8">
<title>norvanTEC – IT Support</title>
<link rel="stylesheet" href="https://fonts.googleapis.com/css2?family=Arimo:ital,wght@0,400;0,700;1,700&family=Cinzel:wght@400&family=PT+Sans&family=Tinos:ital,wght@1,700&display=swap">
<style>
:root{
  --top-bar:#1b1e1e;
  --header-top:#ffffff;
  --header-bottom:#e9e9e9;
  --brand-orange:#f0561c;
  --nav-blue:#1aa7f0;
  --nav-blue-dark:#0f7fe0;
  --nav-text:#1f1f1f;
  --slide-blue:#1fa2e0;
  --slide-cyan:#5ee6fb;
  --tab-one:#1aa6d8;
  --tab-two:#0a7aa3;
  --tab-three:#4f4f4f;
  --heading:#2a2a2a;
  --body-text:#555555;
  --offer-blue:#2ab1d9;
  --rule:#7fcbe0;
  --button-grey:#b9b9b9;
  --footer:#474344;
}
*{margin:0;padding:0;box-sizing:border-box}
html,body{width:1200px;height:1172px;overflow:hidden;background:#fff}
body{position:relative;font-family:"Arimo",Arial,sans-serif;color:var(--body-text)}
.abs{position:absolute}

.top-bar{left:0;top:0;width:1200px;height:48px;background:var(--top-bar)}
.site-header{left:0;top:48px;width:1200px;height:116px;
  background:linear-gradient(var(--header-top),var(--header-bottom));
  box-shadow:0 3px 6px rgba(0,0,0,.12)}
.brand{left:173px;top:96px;font-size:40px;color:var(--brand-orange);letter-spacing:.5px;font-weight:400}

.nav-home{left:645px;top:45px;width:89px;height:101px}
.nav-home span{position:absolute;left:0;top:43px;width:89px;text-align:center;color:#fff;font-weight:700;font-size:14px}
.nav-link{top:89px;font-size:14px;font-weight:700;color:var(--nav-text)}

.slider{left:172px;top:202px;width:840px;height:343px}
.tab{position:absolute;top:0;height:341px;border-radius:6px;box-shadow:2px 3px 5px rgba(0,0,0,.35)}
.tab-testimonials{left:610px;width:78px;background:var(--tab-one)}
.tab-news{left:674px;width:87px;background:var(--tab-two)}
.tab-services{left:749px;width:89px;background:var(--tab-three)}
.tab-label{position:absolute;top:30px;width:100%;height:150px;display:flex;justify-content:center;align-items:center}
.tab-label span{display:block;transform:rotate(-90deg);white-space:nowrap;font-family:"Cinzel",serif;color:#fff;font-size:18px}
.tab-more{position:absolute;top:249px;width:46px;height:70px;border-radius:3px;display:flex;align-items:center;justify-content:center}
.tab-more span{transform:rotate(-90deg);color:#fff;font-size:10px;white-space:nowrap}
.tab-testimonials .tab-more{left:28px;background:#1483b5}
.tab-news .tab-more{left:22px;background:#0a92bf}
.tab-services .tab-more{left:22px;background:#666}
.slide-main{position:absolute;left:0;top:0;width:612px;height:341px;border-radius:7px;
  background:linear-gradient(90deg,var(--slide-blue),var(--slide-cyan));
  box-shadow:2px 3px 5px rgba(0,0,0,.35);overflow:hidden}
.slide-photo{position:absolute;left:0;top:18px;width:450px;height:323px;
  background:radial-gradient(ellipse at 40% 55%,#c9d8ea 0%,#7eb3de 45%,rgba(60,150,220,0) 75%)}
.slide-title{position:absolute;left:349px;top:30px;font-family:"Cinzel",serif;font-size:30px;color:#3a4a56}
.slide-text{position:absolute;left:344px;top:78px;width:231px;font-size:11.5px;line-height:18.5px;color:#4a5b66;text-align:justify}
.slide-more{position:absolute;left:504px;top:159px;width:71px;height:47px;background:#4fb8c8;border-radius:3px;color:#fff;font-size:11px;display:flex;align-items:center;justify-content:center}

.section-title{font-size:21px;color:var(--heading)}
.rule{border-top:1px dashed var(--rule);height:0}
.about-text{left:169px;top:650px;width:591px;font-size:11.5px;line-height:18.7px}
.about-text p+p{margin-top:18.7px}
.offer-text{left:805px;top:640px;width:224px;font-family:"Tinos",serif;font-style:italic;font-weight:700;font-size:17.3px;line-height:22.3px;color:var(--offer-blue);text-align:justify}
.btn{width:78px;height:25px;background:var(--button-grey);color:#fff;font-size:11.5px;border-radius:2px;display:flex;align-items:center;justify-content:center}

.feature-title{font-family:"PT Sans",sans-serif;font-size:21px;color:var(--heading);display:flex;align-items:center;gap:4px}
.feature-text{width:183px;font-size:11.5px;line-height:18.5px;text-align:justify}

.site-footer{left:0;top:1055px;width:1200px;height:117px;background:var(--footer)}
.copyright{left:163px;top:1072px;font-size:11.5px;color:#fff}
.map-pin{left:1016px;top:1067px}
</style>
</head>
<body>
<div class="abs top-bar"></div>
<header class="abs site-header"></header>
<div class="abs brand">norvanTEC</div>

<svg class="abs nav-home" viewBox="0 0 89 101" aria-hidden="true">
  <defs><linearGradient id="homeGrad" x1="0" y1="0" x2="0" y2="1">
    <stop offset="0" stop-color="#26c0f7"/><stop offset="1" stop-color="#0d78e0"/></linearGradient></defs>
  <path d="M0 0H89V101L44.5 86L0 101Z" fill="url(#homeGrad)"/>
</svg>
<nav>
  <div class="abs nav-home" style="pointer-events:none"><span>Home</span></div>
  <span class="abs nav-link" style="left:761px">About us</span>
  <span class="abs nav-link" style="left:852px">Services</span>
  <span class="abs nav-link" style="left:930px">Prices</span>
  <span class="abs nav-link" style="left:995px">Contacts</span>
</nav>

<section class="abs slider">
  <div class="tab tab-services"><div class="tab-label"><span>Best Services</span></div><div class="tab-more"><span>MORE +</span></div></div>
  <div class="tab tab-news"><div class="tab-label"><span>Latest News</span></div><div class="tab-more"><span>MORE +</span></div></div>
  <div class="tab tab-testimonials"><div class="tab-label"><span>Testimonials</span></div><div class="tab-more"><span>MORE +</span></div></div>
  <div class="slide-main">
    <div class="slide-photo" role="img" aria-label="Photo of two colleagues working together at a laptop"></div>
    <div class="slide-title">IT Plan Quote</div>
    <p class="slide-text">Lorem ipsum dolor sit amet, et vocibus feugait adolescens vim, ad cum adolescens accommodare adolescens vim, ad cum adolescens accommodare.</p>
    <div class="slide-more">MORE +</div>
  </div>
</section>

<h2 class="abs section-title" style="left:173px;top:602px">A Few Words About Us</h2>
<div class="abs rule" style="left:169px;top:633px;width:591px"></div>
<div class="abs about-text">
  <p>Lorem ipsum dolor sit amet, et vocibus feugait adolescens vim, ad cum adolescens accommodare.Lorem ipsum dolor sit amet, et vocibus feugait adolescens vim, ad cum adolescens accommodare.</p>
  <p>Lorem ipsum dolor sit amet, et vocibus feugait adolescens vim, ad cum adolescens accommodare.Lorem ipsum dolor sit amet, et vocibus feugait adolescens vim, ad cum adolescens accommodare. Lorem ipsum dolor sit amet, et vocibus feugait adolescens vim, ad cum adolescens accommodare.Lorem ipsum dolor sit amet, et vocibus feugait adolescens vim, ad cum adolescens accommodare.</p>
</div>
<div class="abs btn" style="left:172px;top:806px">More Info</div>

<h2 class="abs section-title" style="left:809px;top:594px">What We Offer</h2>
<div class="abs rule" style="left:809px;top:630px;width:201px"></div>
<div class="abs offer-text">Lorem ipsum dolor sit amet, et vocibus feugait adolescens vim, ad cum adolescens accommodare.<br>Vocibus feugait adolescens vim, ad cum adolescens accommodare.</div>
<div class="abs btn" style="left:810px;top:806px">More Info</div>

<div class="abs rule" style="left:169px;top:865px;width:859px"></div>

<section>
  <div class="abs feature-title" style="left:170px;top:893px">
    <svg width="36" height="30" viewBox="0 0 36 30" aria-hidden="true"><rect x="12" y="2" width="12" height="6" rx="2" fill="none" stroke="#6b3a12" stroke-width="2.5"/><rect x="1" y="7" width="34" height="22" rx="3" fill="#a5581e"/><rect x="1" y="15" width="34" height="2" fill="#6b3a12"/></svg>
    Technology</div>
  <p class="abs feature-text" style="left:169px;top:936px">Lorem ipsum dolor sit amet, et vocibus feugait adolescens vim, ad cum adolescens accommodare.Lorem ipsum dolor sit amet, et vocibus feugait adolescens.</p>

  <div class="abs feature-title" style="left:412px;top:890px">
    <svg width="24" height="36" viewBox="0 0 24 36" aria-hidden="true"><text x="12" y="30" text-anchor="middle" font-family="Arial,sans-serif" font-weight="700" font-size="34" fill="#e8a412">$</text></svg>
    Pricing</div>
  <p class="abs feature-text" style="left:412px;top:936px">Lorem ipsum dolor sit amet, et vocibus feugait adolescens vim, ad cum adolescens accommodare.Lorem ipsum dolor sit amet, et vocibus feugait adolescens.</p>

  <div class="abs feature-title" style="left:618px;top:888px">
    <svg width="26" height="38" viewBox="0 0 26 38" aria-hidden="true"><circle cx="13" cy="11" r="9" fill="#b55a2a"/><path d="M2 37C2 26 24 26 24 37Z" fill="#2f7fd0"/></svg>
    Technical Support</div>
  <p class="abs feature-text" style="left:628px;top:938px">Lorem ipsum dolor sit amet, et vocibus feugait adolescens vim, ad cum adolescens accommodare.Lorem ipsum dolor sit amet, et vocibus feugait adolescens.</p>

  <div class="abs feature-title" style="left:855px;top:886px">
    <svg width="30" height="40" viewBox="0 0 30 40" aria-hidden="true"><circle cx="15" cy="14" r="11" fill="#f3f3e6" stroke="#cfd3c0" stroke-width="1.5"/><rect x="10" y="25" width="10" height="9" rx="1" fill="#b8a442"/></svg>
    IT Plan Quote</div>
  <p class="abs feature-text" style="left:862px;top:938px">Lorem ipsum dolor sit amet, et vocibus feugait adolescens vim, ad cum adolescens accommodare.Lorem ipsum dolor sit amet, et vocibus feugait adolescens.</p>
</section>

<footer class="abs site-footer"></footer>
<div class="abs copyright">Copyright © 2011 Norvantec Pty Ltd</div>
<svg class="abs map-pin" width="26" height="28" viewBox="0 0 26 28" aria-label="Location">
  <rect x="1" y="6" width="24" height="21" rx="2" fill="#f3c13a"/>
  <path d="M1 20L25 12V18L1 26Z" fill="#4aa3e0"/>
  <path d="M9 1a5 5 0 0 1 5 5c0 4-5 9-5 9s-5-5-5-9a5 5 0 0 1 5-5Z" fill="#e23b2c"/>
  <circle cx="9" cy="6" r="1.8" fill="#fff"/>
</svg>
</body>
</html>
```